New packaging company website**

We are looking for a new design for our corporate website (www.cratevendo.it). The theme must be made with Elementor and Crocoblock plugins. Currently the demo site can be reached at www.cratevendo.cloud

You can also check our current site for your reference www.cratevendo.it
We mainly deal with the resale of industrial containers for companies, most of our customers are B2B but also a good number of private customers. The site must therefore be accessible to all and the prices always visible even without registration or other.

Given the heterogeneity of our articles, we need a very clear shop page, with clearly visible filters and possibly with a list view and a table.

However, it does not have to be a simple ecommerce, we still want a site with many texts, spaces for product FAQs, tooltips on filters or attributes.

Target Market(s)

90% B2B

Coding

Coded - Design and coding required

Requirements
Must have
• beautiful, modern and captivating graphics. It must be a "full" site and not a flat one.
Nice to have
• We are undecided about the location of the main product menu.

If you leave the top bar with the icons and labels of the macro categories, as happens now on the live site and on the demo site.

Or if you want to insert the classic "all categories" on the top menu (https://lumberfay.qrivenso.com/demo-tools/demo/tools/ or https://www.havelintheme.com/wordpress/havel/shop30/)

Or if you want to take advantage of something more modern, such as the sidebar menu (https://www.havelintheme.com/wordpress/havel/shop10/ or https://www.havelintheme.com/wordpress/havel/shop19/)

```html
<!DOCTYPE html>
<html lang="en">
<head>
<meta charset="utf-8">
<title>Cratevendo — Industrial Containers</title>
<link href="https://fonts.googleapis.com/css2?family=Montserrat:wght@400;500;600;700&family=Oswald:wght@500;600;700&family=Roboto:ital,wght@0,300;0,400;0,500;0,700;1,300;1,400&display=swap" rel="stylesheet">
<style>
:root{
  --blue:#0f5a88;
  --blue-dark:#0b4a72;
  --red:#d3141c;
  --yellow:#ffd400;
  --ink:#1b1b1b;
  --text:#444;
  --muted:#777;
  --line:#e3e3e3;
  --grey-bg:#efefef;
  --footer:#222;
  --white:#fff;
}
*{box-sizing:border-box;margin:0;padding:0}
html,body{width:1200px;height:3164px;overflow:hidden}
body{font-family:"Roboto",sans-serif;color:var(--text);background:var(--white);position:relative}
.abs{position:absolute}
a{color:inherit;text-decoration:none}

/* top bar */
.topbar{left:0;top:0;width:1200px;height:43px;background:var(--blue);color:#dfe9f1;font-size:14px}
.topbar .links{left:112px;top:0;height:43px;display:flex;align-items:center}
.topbar .links span{padding:0 13px;border-right:1px solid rgba(255,255,255,.35);line-height:26px}
.topbar .links span:first-child{padding-left:0}
.topbar .social{display:flex;gap:10px;padding-left:14px}
.topbar .social i{width:10px;height:10px;background:#fff;border-radius:2px;display:block}
.topbar .right{right:112px;top:0;height:43px;display:flex;align-items:center;gap:14px;font-family:"Montserrat",sans-serif}
.topbar .phone{font-weight:600;color:#fff;font-size:15px;padding-right:14px;border-right:1px solid rgba(255,255,255,.35);display:flex;gap:6px;align-items:center}

/* header */
.brand{left:113px;top:58px;display:flex;align-items:center;gap:10px;font-family:"Montserrat",sans-serif;font-weight:700;font-size:24px;color:var(--blue);letter-spacing:.3px}
.brand i{width:32px;height:32px;background:var(--red);display:block}
.search{left:366px;top:55px;width:470px;height:44px;border:1px solid var(--line);display:flex;font-size:14px;color:#666}
.search .field{flex:1;padding:0 18px;display:flex;align-items:center}
.search .cat{width:133px;border-left:1px solid var(--line);display:flex;align-items:center;padding-left:12px;gap:6px}
.search .go{width:46px;background:var(--red);display:flex;align-items:center;justify-content:center}
.account{left:860px;top:60px;display:flex;align-items:center;gap:14px;font-family:"Montserrat",sans-serif;font-weight:600;font-size:14px;color:var(--ink)}
.cart-badge{position:absolute;right:-7px;top:-6px;width:14px;height:14px;border-radius:50%;background:var(--red);color:#fff;font-size:9px;text-align:center;line-height:14px}

/* nav */
.nav{left:0;top:111px;width:1200px;height:43px;border-top:1px solid var(--line);border-bottom:1px solid var(--line);font-family:"Montserrat",sans-serif;font-size:14px;color:var(--ink)}
.nav .browse{left:112px;top:0;height:42px;width:222px;display:flex;align-items:center;gap:12px;font-weight:600;border-right:1px solid var(--line)}
.nav .menu{left:368px;top:0;height:42px;display:flex;align-items:center;gap:24px;font-weight:500}
.nav .menu span::after{content:" ⌄";font-size:11px}
.nav .menu span.plain::after{content:""}
.nav .addr{right:112px;top:0;height:42px;display:flex;align-items:center;gap:8px;font-weight:600}
.pin{width:30px;height:30px;border-radius:50%;background:var(--red);display:flex;align-items:center;justify-content:center}

/* hero */
.hero{left:0;top:160px;width:1200px;height:405px;background:linear-gradient(90deg,#ededed,#e4e4e4)}
.hero-visual{left:528px;top:0;width:672px;height:405px;background:linear-gradient(120deg,#f4f4f4 0%,#3a86e0 40%,#1f63c4 60%,#c9c9c9 85%,#e7e7e7 100%)}
.hero h1{left:117px;top:56px;font-family:"Oswald",sans-serif;font-weight:700;font-size:72px;line-height:68px;color:#111;letter-spacing:.5px}
.price-tag{left:112px;top:215px;width:172px;height:51px;background:var(--yellow);font-family:"Montserrat",sans-serif;font-style:italic;font-weight:700;font-size:42px;line-height:51px;padding-left:6px;color:#111}
.price-tag sup{font-size:22px}
.hero .cta{left:112px;top:288px;width:264px;height:52px;background:var(--red);color:#fff;font-family:"Montserrat",sans-serif;font-weight:600;font-size:17px;display:flex;align-items:center;justify-content:center}
.hero .arrow{top:188px}
.dots{left:556px;top:370px;display:flex;gap:8px}
.dots i{width:11px;height:11px;border-radius:50%;background:#9cc3dc;display:block}
.dots i:first-child{background:var(--blue)}

/* trust bar */
.trust{left:0;top:565px;width:1200px;height:98px;display:flex;align-items:center;justify-content:center}
.trust .item{display:flex;align-items:center;gap:10px;padding:0 36px;border-right:1px solid var(--line);height:52px}
.trust .item:last-child{border-right:0}
.trust b{display:block;font-family:"Montserrat",sans-serif;font-weight:700;font-size:14px;color:var(--ink);letter-spacing:.2px}
.trust small{display:block;font-size:12px;color:var(--muted);line-height:14px}
.trust .red{color:var(--red);font-weight:600}

/* intro */
.intro h2{left:0;top:716px;width:1200px;text-align:center;font-family:"Oswald",sans-serif;font-weight:600;font-size:33px;color:#111;letter-spacing:.3px}
.intro p{left:190px;top:767px;width:820px;text-align:center;font-size:14px;line-height:26px;color:#666}
.intro p b{color:#111;font-weight:500;font-size:15px}

/* category cards */
.cat-card{width:477px;height:245px;background:#fff;box-shadow:0 2px 10px rgba(0,0,0,.08)}
.cat-card h3{position:absolute;left:20px;top:20px;font-family:"Montserrat",sans-serif;font-weight:700;font-size:18px;color:#111;letter-spacing:.3px}
.cat-card ul{position:absolute;left:21px;top:57px;list-style:none;font-size:15px;line-height:26px;color:#333}
.cat-card .see{position:absolute;left:20px;top:194px;width:112px;height:32px;background:var(--red);color:#fff;font-family:"Montserrat",sans-serif;font-weight:700;font-size:15px;display:flex;align-items:center;justify-content:center}
.cat-card .pic{position:absolute;right:16px;top:26px;width:150px;height:196px;border-radius:4px}
.btn-red{background:var(--red);color:#fff;font-family:"Montserrat",sans-serif;font-weight:600;font-size:17px;display:flex;align-items:center;justify-content:center}

/* featured product */
.featured{left:0;top:1550px;width:1200px;height:560px;background:var(--grey-bg)}
.bottle{left:247px;top:46px;width:136px;height:440px;border-radius:40px 40px 30px 30px;background:linear-gradient(180deg,#f3f3f3 0%,#f3f3f3 12%,#4bb07a 25%,#2f9a63 70%,#3fa874 100%)}
.featured h3{left:510px;top:66px;width:520px;font-family:"Montserrat",sans-serif;font-weight:700;font-size:22px;line-height:31px;color:#1b1b1b;letter-spacing:.2px}
.featured .price{left:511px;top:169px;width:90px;height:37px;background:var(--blue);color:#fff;font-family:"Montserrat",sans-serif;font-weight:700;font-size:26px;line-height:37px;text-align:center}
.featured .price small{font-size:18px;font-weight:500}
.specs{left:511px;top:224px;border-collapse:collapse}
.specs td{height:34px;font-size:16px;color:#333;vertical-align:middle}
.specs td:first-child{width:276px;font-family:"Montserrat",sans-serif;font-weight:700;font-size:16px;color:#111}
.featured .add{left:507px;top:433px;width:180px;height:52px}
.chev{top:220px}

/* testimonials */
.clients{left:0;top:2110px;width:1200px;height:442px;background:var(--blue)}
.clients h2{left:0;top:70px;width:1200px;text-align:center;font-family:"Roboto",sans-serif;font-weight:700;font-size:40px;color:#fff}
.quote{top:146px;width:317px;height:225px;background:#fff}
.quote .mark{position:absolute;left:22px;top:30px;font-family:"Oswald",sans-serif;font-size:56px;line-height:40px;color:var(--red);font-weight:700}
.quote p{position:absolute;left:62px;top:22px;width:233px;font-style:italic;font-weight:300;font-size:15px;line-height:29px;color:#333}
.quote .who{position:absolute;left:24px;top:153px;display:flex;align-items:center;gap:14px}
.avatar{width:48px;height:48px;border-radius:50%;background:linear-gradient(#8a8a8a,#3d3d3d)}
.who b{display:block;font-weight:500;font-size:16px;color:#222}
.stars{color:#f0b400;font-size:14px;letter-spacing:1px}

/* signup */
.signup h2{left:0;top:2623px;width:1200px;text-align:center;font-family:"Roboto",sans-serif;font-weight:700;font-size:31px;color:#111}
.signup h2 span{font-weight:400}
.signup p{left:0;top:2668px;width:1200px;text-align:center;font-family:"Montserrat",sans-serif;font-weight:500;font-size:15px;color:#666}
.signup .form{left:281px;top:2714px;width:623px;height:52px;border:1px solid #d6d6d6;display:flex}
.signup .form span{flex:1;padding-left:25px;display:flex;align-items:center;font-size:14px;color:#666;font-family:"Montserrat",sans-serif}
.signup .form b{width:143px;background:var(--red);color:#fff;font-family:"Montserrat",sans-serif;font-weight:600;font-size:17px;display:flex;align-items:center;justify-content:center}

/* footer */
.footer{left:0;top:2843px;width:1200px;height:321px;background:var(--footer);color:#ddd}
.footer h4{position:absolute;top:52px;font-family:"Montserrat",sans-serif;font-weight:600;font-size:16px;letter-spacing:2px;color:#fff;border-left:2px solid var(--red);border-right:2px solid var(--red);padding:0 10px;line-height:16px}
.footer ul{position:absolute;top:94px;list-style:none;font-size:13px;line-height:27px;color:#ccc}
.footer .contact{position:absolute;left:104px;top:94px;font-family:"Montserrat",sans-serif;font-size:14px;color:#ddd;line-height:22px}
.footer .contact div{display:flex;gap:14px;margin-bottom:14px}
.footer .rule{position:absolute;left:104px;top:248px;width:992px;height:1px;background:#3a3a3a}
.footer .copy{position:absolute;left:104px;top:280px;font-size:13px;color:#aaa}
.pay{position:absolute;left:507px;top:272px;display:flex;gap:3px}
.pay i{width:40px;height:26px;display:block;border-radius:2px}
.fsocial{position:absolute;left:865px;top:268px;display:flex;gap:11px}
.fsocial i{width:34px;height:34px;border-radius:50%;background:#3b3b3b;display:block}
</style>
</head>
<body>

<!-- top bar -->
<div class="abs topbar">
  <div class="abs links">
    <span>Newsletter</span><span>Contact Us</span><span>FAQs</span>
    <div class="social"><i></i><i></i><i></i><i></i></div>
  </div>
  <div class="abs right">
    <div class="phone">
      <svg width="12" height="12" viewBox="0 0 24 24"><path fill="#fff" d="M6.6 10.8a15.1 15.1 0 006.6 6.6l2.2-2.2c.3-.3.7-.4 1-.2 1.1.4 2.3.6 3.6.6.6 0 1 .4 1 1V20c0 .6-.4 1-1 1A17 17 0 013 4c0-.6.4-1 1-1h3.5c.6 0 1 .4 1 1 0 1.3.2 2.5.6 3.6.1.3 0 .7-.2 1z"/></svg>
      02/55501234
    </div>
    <span>English ⌄</span>
  </div>
</div>

<!-- header -->
<div class="abs brand"><i></i>CRATEVENDO</div>
<div class="abs search">
  <div class="field">Search Products</div>
  <div class="cat">select category ⌄</div>
  <div class="go"><svg width="22" height="22" viewBox="0 0 24 24" fill="none" stroke="#fff" stroke-width="2"><circle cx="10.5" cy="10.5" r="7"/><path d="M16 16l5 5"/></svg></div>
</div>
<div class="abs account">
  <span>Login/Register</span>
  <svg width="28" height="26" viewBox="0 0 24 24" fill="none" stroke="#222" stroke-width="1.4"><path d="M12 21s-8-5.3-8-11a4.5 4.5 0 018-2.8A4.5 4.5 0 0120 10c0 5.7-8 11-8 11z"/></svg>
  <svg width="24" height="26" viewBox="0 0 24 24" fill="none" stroke="#222" stroke-width="1.4"><circle cx="12" cy="8" r="4"/><path d="M4 22c0-4.4 3.6-8 8-8s8 3.6 8 8"/></svg>
  <span style="position:relative"><svg width="26" height="26" viewBox="0 0 24 24" fill="none" stroke="#222" stroke-width="1.4"><path d="M2 3h3l2.5 12h11L21 7H6.2"/><circle cx="9" cy="19.5" r="1.5"/><circle cx="17" cy="19.5" r="1.5"/></svg><span class="cart-badge">0</span></span>
</div>

<!-- nav -->
<div class="abs nav">
  <div class="abs browse">
    <svg width="22" height="18" viewBox="0 0 22 18"><path d="M0 1h22M0 9h22M0 17h22" stroke="#222" stroke-width="2"/></svg>
    Browse Categories <span style="margin-left:14px">⌄</span>
  </div>
  <div class="abs menu"><span>Home</span><span>Shop</span><span>Blog</span><span>Pages</span><span>Elements</span><span class="plain">Buy</span></div>
  <div class="abs addr">
    <div class="pin"><svg width="14" height="16" viewBox="0 0 24 24"><path fill="#fff" d="M12 2a7 7 0 00-7 7c0 5 7 13 7 13s7-8 7-13a7 7 0 00-7-7zm0 9.5A2.5 2.5 0 1112 6.5a2.5 2.5 0 010 5z"/></svg></div>
    123 Avenue name, City name
  </div>
</div>

<!-- hero -->
<section class="abs hero">
  <div class="abs hero-visual" role="img" aria-label="Plastic tanks, blue drums and an IBC container"></div>
  <h1 class="abs">CISTERNE IN<br>PLASTICA</h1>
  <div class="abs price-tag">€133<sup>.00</sup></div>
  <a class="abs cta">VEDI TUTTI I MODELLI</a>
  <svg class="abs arrow" style="left:70px" width="18" height="32" viewBox="0 0 18 32"><path d="M16 2L2 16l14 14" fill="none" stroke="#222" stroke-width="2"/></svg>
  <svg class="abs arrow" style="left:1108px" width="18" height="32" viewBox="0 0 18 32"><path d="M2 2l14 14L2 30" fill="none" stroke="#222" stroke-width="2"/></svg>
  <div class="abs dots"><i></i><i></i><i></i><i></i><i></i></div>
</section>

<!-- trust bar -->
<div class="abs trust">
  <div class="item">
    <svg width="38" height="30" viewBox="0 0 38 30" fill="none" stroke="#333" stroke-width="1.5"><rect x="2" y="8" width="22" height="14"/><path d="M24 12h7l5 5v5H24"/><circle cx="9" cy="24" r="3" fill="#fff"/><circle cx="30" cy="24" r="3" fill="#fff"/></svg>
    <div><b>FAST SHIPPING</b><small>Deliveries throughout Italy</small></div>
  </div>
  <div class="item">
    <svg width="30" height="30" viewBox="0 0 30 30" fill="none" stroke="#333" stroke-width="1.5"><path d="M5 17v-3a10 10 0 0120 0v3"/><rect x="3" y="16" width="5" height="8" rx="2"/><rect x="22" y="16" width="5" height="8" rx="2"/></svg>
    <div><b>CUSTOMER SERVICE</b><small>From9:00 to 13:00 &nbsp;<span class="red">☎ 02/55501234</span></small></div>
  </div>
  <div class="item">
    <svg width="30" height="32" viewBox="0 0 30 32" fill="none" stroke="#333" stroke-width="1.5"><rect x="4" y="2" width="20" height="26"/><path d="M8 9h12M8 14h12M8 19h8"/><circle cx="22" cy="24" r="4" fill="#fff"/></svg>
    <div><b>CERTIFIED PRODUCTS</b><small>Guaranteed, of quality and in<br>accordance with the law</small></div>
  </div>
  <div class="item">
    <svg width="40" height="32" viewBox="0 0 40 32" fill="none" stroke="#333" stroke-width="1.5"><rect x="2" y="4" width="30" height="20" rx="2"/><path d="M2 10h30"/><path d="M28 16l8 3v5c0 4-4 6-4 6s-4-2-4-6z" fill="#f5c400"/></svg>
    <div><b>SECURE PAYMNETS</b><small><span style="color:#111;font-weight:700;font-size:14px">E-wallet,</span> credit card, Bank Transfer,<br>Cash on Delivery</small></div>
  </div>
</div>

<!-- intro -->
<section class="intro">
  <h2 class="abs">CRATEVENDO ONLINE SALE OF SUPPLIES FOR BODIES &amp; COMPANIES</h2>
  <p class="abs">Plastic Containers, Metal Containers, Shelves, Lockers, Safety &amp; Environment, <b>Pallets And Benches,</b> Packaging Products, First Aid, Accident Prevention and PPE <b>Delivery in 24 / 48H</b> throughout Italy. Products at the <b>best price</b>, for the proper functioning of every institution and company.</p>
</section>

<!-- categories -->
<div class="abs cat-card" style="left:110px;top:869px">
  <h3>METAL CONTAINERS</h3>
  <ul><li>Metal Containers</li><li>Tinplate Cans</li><li>Buckets And Tipper Containers</li><li>Metal Drums</li><li>Metal Containers With Opening Bottom</li></ul>
  <div class="pic" role="img" aria-label="Orange metal container with tinplate cans and bucket" style="width:140px;background:linear-gradient(135deg,#e8622a 0%,#d9541d 55%,#bcbcbc 75%,#ececec 100%)"></div>
  <a class="see">SEE ALL</a>
</div>
<div class="abs cat-card" style="left:608px;top:869px">
  <h3>PLASTIC CONTAINERS</h3>
  <ul><li>Plastic Jars</li><li>Plastic Tipper Buckets</li><li>Plastic Drums And Drums</li><li>Plastic Bottles And Bottles</li><li>Plastic Carboys</li></ul>
  <div class="pic" role="img" aria-label="Blue plastic tanks and white IBC container" style="width:200px;top:54px;height:168px;background:linear-gradient(135deg,#2d8ee6 0%,#1b6fd0 55%,#e2e2e2 80%,#f2f2f2 100%)"></div>
  <a class="see">SEE ALL</a>
</div>
<div class="abs cat-card" style="left:110px;top:1133px">
  <h3>TECHNICAL FURNITURE</h3>
  <ul><li>Wardrobes</li><li>Work Benches And Tables</li><li>Drawers, Filing Cabinets And Cartelliere</li><li>Visual Communication</li><li>Benches For Changing Rooms</li></ul>
  <div class="pic" role="img" aria-label="Grey steel lockers and blue workbench" style="width:130px;background:linear-gradient(160deg,#d8d8d8 0%,#bdbdbd 50%,#1e73c8 80%,#1a63b0 100%)"></div>
  <a class="see">SEE ALL</a>
</div>
<div class="abs cat-card" style="left:608px;top:1133px">
  <h3>TORVIK TOOLS</h3>
  <ul><li>Containers And Assortments</li><li>Operating Keys</li><li>Sockets And Accessories</li><li>Torque Wrenches And Multipliers</li><li>Screwdrivers, Male Keys And Inserts</li></ul>
  <div class="pic" role="img" aria-label="Orange tool trolley with assorted tools" style="width:150px;background:linear-gradient(160deg,#3a3a3a 0%,#f08a1d 45%,#2b2b2b 70%,#f29a2e 100%)"></div>
  <a class="see">SEE ALL</a>
</div>

<a class="abs btn-red" style="left:510px;top:1414px;width:180px;height:52px">VIEW ALL</a>

<!-- featured product -->
<section class="abs featured">
  <div class="abs bottle" role="img" aria-label="Bottle of green hand sanitising gel, 500 ml"></div>
  <svg class="abs chev" style="left:92px" width="56" height="100" viewBox="0 0 56 100"><path d="M54 2L4 50l50 48" fill="none" stroke="#555" stroke-width="2"/></svg>
  <svg class="abs chev" style="left:1078px" width="56" height="100" viewBox="0 0 56 100"><path d="M2 2l50 48L2 98" fill="none" stroke="#555" stroke-width="2"/></svg>
  <h3 class="abs">BACTERICIDAL &amp; VIRUCIDAL DISINFECTANT HAND GEL, 60% ALCOHOL, SIZE 500 ML, TO BE USED WITHOUT WATER</h3>
  <div class="abs price"><small>€</small>6.59</div>
  <table class="abs specs">
    <tr><td>ITEM CODE:</td><td>UB610</td></tr>
    <tr><td>CONDITION:</td><td>New</td></tr>
    <tr><td>INFORMATION:</td><td>Medical Surgery - 60% Alcohol</td></tr>
    <tr><td>FEATURES:</td><td>UB610</td></tr>
    <tr><td>MINIMUM ORDER QUANTITY:</td><td>1</td></tr>
    <tr><td>ITEM CODE:</td><td>8001234567890</td></tr>
  </table>
  <a class="abs btn-red add">ADD TO CART</a>
</section>

<!-- testimonials -->
<section class="abs clients">
  <h2 class="abs">WHAT OUR CLIENTS SAY</h2>
  <svg class="abs" style="left:70px;top:244px" width="32" height="22" viewBox="0 0 32 22"><path d="M31 11H2M11 2L2 11l9 9" fill="none" stroke="#fff" stroke-width="2.5"/></svg>
  <svg class="abs" style="left:1098px;top:244px" width="32" height="22" viewBox="0 0 32 22"><path d="M1 11h29M21 2l9 9-9 9" fill="none" stroke="#fff" stroke-width="2.5"/></svg>
  <div class="abs quote" style="left:112px">
    <div class="mark">“</div>
    <p>220 liter cylindrical iron drum, full opening, ADR / ONU approved for solids, blue body and raw interior (lid included)"</p>
    <div class="who"><div class="avatar"></div><div><b>- Laura Conti</b><div class="stars">★★★★★</div></div></div>
  </div>
  <div class="abs quote" style="left:441px">
    <div class="mark">“</div>
    <p>Cassetta in plastica (PP) sovrapponibile, 10 Lt, mis. 600 L x 400 P x 60 H mm, base e pareti chiuse, maniglie chiuse</p>
    <div class="who"><div class="avatar"></div><div><b>- Laura Conti</b><div class="stars">★★★★★</div></div></div>
  </div>
  <div class="abs quote" style="left:771px">
    <div class="mark">“</div>
    <p>Cassa pallet in plastica (HDPE) 4 piedi, Mis. 1200 L x 800 P x 800 H mm, capacità 530 Lt, portata 250 Kg (Polietilene Alta Densità</p>
    <div class="who"><div class="avatar"></div><div><b>- Laura Conti</b><div class="stars">★★★★★</div></div></div>
  </div>
</section>

<!-- signup -->
<section class="signup">
  <h2 class="abs">SIGN UP SPECIAL <span>PROMOTIONS</span></h2>
  <p class="abs">Get exclusive deals you wont find anywhere else straight to your inbox!</p>
  <div class="abs form"><span>Enter Your Email Address</span><b>SUBSCRIBE</b></div>
</section>

<!-- footer -->
<footer class="abs footer">
  <h4 style="left:104px">CONTACT</h4>
  <h4 style="left:432px">MY ACCOUNT</h4>
  <h4 style="left:679px">INFORMATION</h4>
  <h4 style="left:933px">OUR SUPPORT</h4>
  <div class="contact">
    <div><svg width="20" height="22" viewBox="0 0 24 24" fill="none" stroke="#aaa" stroke-width="1.5"><path d="M12 2a7 7 0 00-7 7c0 5 7 13 7 13s7-8 7-13a7 7 0 00-7-7z"/><circle cx="12" cy="9" r="2.5"/></svg><span>123 Avenue name, City<br>name 10150, United States</span></div>
    <div><svg width="20" height="20" viewBox="0 0 24 24" fill="none" stroke="#aaa" stroke-width="1.5"><path d="M22 2L2 10l8 3 3 8z"/></svg><span>info@cratevendo.com</span></div>
    <div><svg width="20" height="24" viewBox="0 0 24 24" fill="none" stroke="#aaa" stroke-width="1.5"><rect x="6" y="1" width="12" height="22" rx="2"/></svg><span>02/55501234</span></div>
  </div>
  <ul style="left:432px"><li>My Account</li><li>Wishlist</li><li>Shoppingcart</li><li>checkout</li><li>My orders</li></ul>
  <ul style="left:679px"><li>About Us</li><li>Top Sellers</li><li>Special Products</li><li>Privacy Policy</li><li>Delivery Information</li></ul>
  <ul style="left:933px"><li>Contact Us</li><li>Shipping &amp; Taxes</li><li>Return Policy</li><li>Site Map</li><li>Contact Us</li></ul>
  <div class="rule"></div>
  <div class="copy">Copyright © 2021 - cratevendo. - All Rights Reserved</div>
  <div class="pay"><i style="background:#fff"></i><i style="background:#e85a2a"></i><i style="background:#2a6fd0"></i><i style="background:#f2c200"></i><i style="background:#fff"></i></div>
  <div class="fsocial"><i></i><i></i><i></i><i></i><i></i></div>
</footer>

</body>
</html>
```